Personal Injury Funding Flyer

We are Qorva Financial, a provider of receivables management solutions to the surgical industry.
We want a 1 page flyer to showcase our Motor Vehicle Accident (MVA) and Personal Injury (PI) case management and lien purchasing.

1- a flyer from a competitor. We like the overall feel of the flyer and the simplicity of the information presented.

You can also check out our website for examples of our company's style
www.qorvafinancial-example.com

Target Market(s)

Surgeons, office managers, administrators and CFOS at smaller surgical facilities and surgical hospitals nationwide

Industry/Entity Type

Financial

Requirements
Must have
• Titled: Personal Injury Case Funding
• Tagline: We Ensure Your Cases are Financially Sound
• Include Qorva Financial's logo
• Be sure to boldly highlight the 3 points:
• 3 Steps to Successful PI Case Management
• 1) Evaluate Cases
• Evaluate the financial aspects of the case including policy limits.
• 2) Consult Attorneys
• Evaluate the case background and likelihood of settlement.
• 3) Guaranteed Funding
• 15 day funding on most cases.
• How Does MVA/PI Funding Work?
• We pay you upfront and wait for the case to settle.
• Our funding eliminates the risk, hassle and uncertainty associated with PI cases.
• You get paid 100% NON-RECOURSE
• Include contact phone number (800) 472-5190
• >No Hassles
• >No Risk
• >Guaranteed Funds.
Nice to have
• Smiling doctor picture
Should not have
• Too much information

```html
<!DOCTYPE html>
<html lang="en">
<head>
<meta charset="utf-8">
<title>Personal Injury Case Funding — Qorva Financial</title>
<link rel="stylesheet" href="https://fonts.googleapis.com/css2?family=Raleway:ital,wght@0,400;0,500;0,600;0,700;0,800;0,900;1,800&display=swap">
<style>
  :root {
    --navy: #13132e;
    --maroon: #4b1816;
    --grey-text: #7a7a7a;
    --body-text: #333333;
    --paper: #ffffff;
    --stage: #e9e7e4;
    --photo-light: #eef4f8;
    --photo-mid: #c9dbe7;
    --photo-deep: #8fb4cc;
  }
  * { box-sizing: border-box; margin: 0; padding: 0; }
  html, body { width: 996px; height: 1200px; overflow: hidden; }
  body {
    background: var(--stage);
    font-family: "Raleway", Arial, sans-serif;
    color: var(--navy);
    position: relative;
  }
  .flyer {
    position: absolute;
    left: 105px; top: 40px;
    width: 800px; height: 1135px;
    background: var(--paper);
    box-shadow: 0 4px 18px rgba(0,0,0,.25);
    overflow: hidden;
  }
  .title-tab { position: absolute; left: 0; top: 0; width: 800px; height: 110px; }
  .title {
    position: absolute; left: 0; top: 26px; width: 800px;
    text-align: center; font-size: 37px; font-weight: 800; letter-spacing: .5px;
  }
  .title .accent { color: var(--maroon); }
  .hero-photo {
    position: absolute; left: 0; top: 110px; width: 800px; height: 425px;
    background:
      radial-gradient(ellipse at 25% 55%, var(--paper) 0%, rgba(255,255,255,0) 45%),
      linear-gradient(100deg, var(--photo-mid) 0%, var(--photo-light) 40%, var(--photo-deep) 70%, var(--photo-light) 100%);
  }
  .recourse { position: absolute; right: 28px; top: 124px; text-align: right; }
  .recourse .paid { font-size: 35px; font-weight: 700; color: var(--grey-text); line-height: 1.1; }
  .recourse .paid strong { color: var(--maroon); font-weight: 800; }
  .recourse .non { font-size: 38px; font-weight: 900; color: var(--navy); line-height: 1.1; letter-spacing: .5px; }
  .benefits-bubble {
    position: absolute; left: 505px; top: 255px; width: 420px; height: 230px;
    background: var(--paper); border-radius: 120px 0 0 120px;
  }
  .benefits { position: absolute; left: 545px; top: 300px; list-style: none; }
  .benefits li {
    display: flex; align-items: flex-start; gap: 10px;
    font-size: 27px; font-weight: 800; font-style: italic; line-height: 1;
    margin-bottom: 13px; color: var(--navy);
  }
  .benefits svg { flex: none; margin-top: 3px; }
  .how { position: absolute; left: 0; top: 548px; width: 800px; text-align: center; }
  .how h2 { font-size: 37px; font-weight: 800; line-height: 1.2; }
  .how .lead { font-size: 23.5px; font-weight: 700; color: var(--grey-text); line-height: 1.2; }
  .how .tagline { font-size: 22.5px; font-weight: 500; color: var(--maroon); margin-top: 4px; }
  .lower { position: absolute; left: 0; top: 660px; width: 800px; height: 475px; }
  .steps-head { position: absolute; left: 0; top: 700px; width: 800px; text-align: center; }
  .steps-head .count { font-size: 40px; font-weight: 900; color: var(--maroon); letter-spacing: .5px; line-height: 1.2; }
  .steps-head .count b { font-size: 52px; }
  .steps-head .sub { font-size: 25.5px; font-weight: 800; letter-spacing: .2px; line-height: 1.2; }
  .step { position: absolute; top: 818px; width: 200px; }
  .step .num {
    position: absolute; left: 0; top: 0; width: 62px; height: 62px; border-radius: 50%;
    background: var(--navy); color: var(--paper);
    display: flex; align-items: center; justify-content: center;
    font-size: 32px; font-weight: 800;
  }
  .step h3 {
    position: absolute; left: 70px; top: 5px; font-size: 19.5px; font-weight: 800; line-height: 1.3; white-space: nowrap;
  }
  .step p {
    position: absolute; left: 8px; top: 76px; width: 185px;
    font-size: 15.5px; font-weight: 500; line-height: 1.35; color: var(--body-text);
  }
  .step-1 { left: 68px; }
  .step-2 { left: 285px; }
  .step-3 { left: 497px; }
  .brand {
    position: absolute; left: 0; top: 1000px; width: 800px;
    text-align: center; font-size: 30px; font-weight: 800; color: var(--navy);
  }
  .contact { position: absolute; left: 0; top: 1040px; width: 800px; text-align: center; }
  .contact .phone { font-size: 37px; font-weight: 800; color: var(--navy); line-height: 1.2; }
  .contact .phone span { color: var(--maroon); }
  .contact .web { font-size: 18px; font-weight: 800; color: var(--navy); }
</style>
</head>
<body>
  <main class="flyer">
    <div class="hero-photo" role="img" aria-label="Smiling doctor with stethoscope in front of a softly blurred medical team in a bright clinic"></div>

    <svg class="title-tab" viewBox="0 0 800 110" aria-hidden="true">
      <defs>
        <filter id="tab-shadow" x="-5%" y="-20%" width="110%" height="160%">
          <feDropShadow dx="0" dy="4" stdDeviation="5" flood-opacity=".25"/>
        </filter>
      </defs>
      <path d="M0 0 H800 V110 H0 Z" fill="#ffffff"/>
      <path d="M38 0 L58 72 Q62 92 84 92 H716 Q738 92 742 72 L762 0 Z" fill="#ffffff" filter="url(#tab-shadow)"/>
    </svg>
    <h1 class="title">PERSONAL INJURY <span class="accent">CASE FUNDING</span></h1>

    <div class="recourse">
      <p class="paid">You get paid <strong>100%</strong></p>
      <p class="non">NON-RECOURSE</p>
    </div>

    <div class="benefits-bubble"></div>
    <ul class="benefits">
      <li><svg width="28" height="24" viewBox="0 0 28 24"><path d="M2 13 L10 21 L26 3" fill="none" stroke="#13132e" stroke-width="5" stroke-linejoin="round"/></svg>HASSLE FREE</li>
      <li><svg width="28" height="24" viewBox="0 0 28 24"><path d="M2 13 L10 21 L26 3" fill="none" stroke="#13132e" stroke-width="5" stroke-linejoin="round"/></svg>RISK FREE</li>
      <li><svg width="28" height="24" viewBox="0 0 28 24"><path d="M2 13 L10 21 L26 3" fill="none" stroke="#13132e" stroke-width="5" stroke-linejoin="round"/></svg>GUARANTEED<br>FUNDS</li>
    </ul>

    <section class="how">
      <h2>How Does MVA/PI Funding Work?</h2>
      <p class="lead">We pay you upfront and wait for the case to settle.</p>
      <p class="tagline">We ensure your cases are financially sound</p>
    </section>

    <svg class="lower" viewBox="0 0 800 475" aria-hidden="true">
      <defs>
        <linearGradient id="lower-fill" x1="0" y1="0" x2="0" y2="1">
          <stop offset="0" stop-color="#e2e2e2"/>
          <stop offset=".5" stop-color="#f1f1f1"/>
          <stop offset="1" stop-color="#fbfbfb"/>
        </linearGradient>
        <filter id="edge-shadow" x="-5%" y="-10%" width="110%" height="120%">
          <feDropShadow dx="0" dy="-2" stdDeviation="3" flood-opacity=".18"/>
        </filter>
      </defs>
      <path d="M0 16 Q400 -4 800 16 V475 H0 Z" fill="url(#lower-fill)" filter="url(#edge-shadow)"/>
    </svg>

    <div class="steps-head">
      <p class="count"><b>3</b> STEPS</p>
      <p class="sub">TO SUCCESSFUL PI CASE MANAGEMENT</p>
    </div>

    <div class="step step-1">
      <span class="num">1</span>
      <h3>EVALUATE<br>CASES</h3>
      <p>Evaluate the financial aspects of the case including policy limits.</p>
    </div>
    <div class="step step-2">
      <span class="num">2</span>
      <h3>CONSULT<br>ATTORNEYS</h3>
      <p>Evaluate the case background and likelihood of settlement.</p>
    </div>
    <div class="step step-3">
      <span class="num">3</span>
      <h3>GUARANTEED<br>FUNDING</h3>
      <p>15 day funding on most cases.</p>
    </div>

    <p class="brand">Qorva Financial</p>

    <div class="contact">
      <p class="phone">(800) <span>472-5190</span></p>
      <p class="web">www.qorvafinancial-example.com</p>
    </div>
  </main>
</body>
</html>
```